Corvane Collective Web Presence Design and Relaunch

Take existing web files and "clean up" for a a more presentable web landing pad.
posted presently on a site pad CSS template. at www.corvanecollective.org

The site is clunky and unprofessional looking. Needs to be toned down so the urgency is conveyed, but not via a burning planet image.

Target Market(s)

Non-profit climate adaptation group targeting local government land management agencies, special districts and private landholders of natural resource properties.

Industry/Entity Type

Environment

Coding

Coded - Design and coding required

Number of Pages Required

4 page

Font styles to use
Serif
Sans Serif

Requirements
Must have
• Include current logos, aspects if content on current site www.corvanecollective.org
• A regional Pacific Northwest Focus (US & Canada). Content speaking to urgency but respectful of cultural diversity and norms. Sustainability themes. Emphasis on action and implementation.
Nice to have
• link to like minded projects. Appear to future generations. Diversity in thematic areas ecological resiliency, energy, food security and infrastructure.

```html
<!DOCTYPE html>
<html lang="en">
<head>
<meta charset="utf-8">
<title>Corvane Collective — Climate Adaptation</title>
<link href="https://fonts.googleapis.com/css2?family=Lato:wght@400;700;900&family=Roboto:wght@400;500;700&display=swap" rel="stylesheet">
<style>
:root{
  --blue:#0a88cf;
  --blue-dark:#066fae;
  --green:#94c83d;
  --green-stat:#a6cf4c;
  --orange:#f47a20;
  --ink:#2b2b2b;
  --text:#6b6b6b;
  --light:#f3f4f6;
  --footer:#2f3133;
  --white:#ffffff;
}
*{box-sizing:border-box;margin:0;padding:0}
html,body{width:1200px;height:4552px;overflow:hidden}
body{position:relative;font-family:"Roboto",sans-serif;color:var(--text);background:var(--white)}
a{color:inherit;text-decoration:none}

/* header */
.site-header{position:absolute;left:0;top:0;width:1200px;height:150px;border-top:4px solid var(--green);background:var(--white)}
.brand{position:absolute;left:112px;top:72px;font-family:"Lato",sans-serif;font-weight:900;font-size:21px;line-height:24px;color:var(--blue);letter-spacing:1px}
.brand-dot{position:absolute;left:148px;top:20px;width:44px;height:44px;border-radius:50%;background:var(--green)}
.call{position:absolute;left:766px;top:22px;display:flex;align-items:center;gap:12px;font-size:14px;color:var(--ink)}
.call strong{font-size:21px;font-weight:500}
.call-icon{width:46px;height:46px;border-radius:50%;border:1px solid #d5e6f2;display:flex;align-items:center;justify-content:center}
.nav{position:absolute;left:350px;top:100px}
.nav a{font-size:14px;color:var(--ink);position:absolute;white-space:nowrap}
.nav a.active{color:var(--blue)}
.nav a.active::after{content:"";position:absolute;left:-4px;right:-4px;top:24px;height:3px;background:var(--blue)}
.btn{display:inline-flex;align-items:center;justify-content:center;border-radius:26px;color:var(--white);font-weight:700;font-size:13px}
.quote{position:absolute;left:944px;top:85px;width:143px;height:48px;background:var(--blue)}

/* hero */
.hero{position:absolute;left:0;top:150px;width:1200px;height:516px;background:linear-gradient(180deg,#7fb3dc 0%,#b9d6ea 28%,#3e5a45 48%,#1f3328 60%,#6a8ea9 74%,#2b4536 100%)}
.hero-panel{position:absolute;left:110px;top:92px;width:510px;height:310px;background:rgba(120,130,140,.55)}
.hero-kicker{position:absolute;left:152px;top:136px;color:var(--white);font-family:"Lato",sans-serif;font-size:21px}
.hero-title{position:absolute;left:152px;top:170px;color:var(--white);font-family:"Lato",sans-serif;font-weight:900;font-size:43px;line-height:52px}
.hero-btn{position:absolute;left:152px;top:285px;width:143px;height:44px;background:var(--blue)}
.dots{position:absolute;left:577px;top:436px;display:flex;gap:6px}
.dots span{width:11px;height:11px;border-radius:50%;background:var(--white)}
.dots span.on{background:var(--blue)}

/* about */
.about-art{position:absolute;left:57px;top:724px;width:505px;height:474px;background:linear-gradient(180deg,#e4f0d2 0%,#dcebf5 100%)}
.section-title{font-family:"Lato",sans-serif;font-weight:700;font-size:31px;color:var(--blue);letter-spacing:.3px}
.section-title span{color:var(--green)}
.rule{width:60px;height:3px;background:var(--blue)}
.about-title{position:absolute;left:599px;top:758px}
.about-rule{position:absolute;left:599px;top:810px}
.about-text{position:absolute;left:599px;top:836px;width:474px;font-size:13px;line-height:28.3px;text-align:justify}
.vision{position:absolute;left:599px;top:1053px;width:127px;height:46px;background:var(--blue)}
.volunteers{position:absolute;left:737px;top:1053px;width:127px;height:46px;background:var(--green)}

/* featured */
.featured{position:absolute;left:0;top:1198px;width:1200px;height:606px;background:linear-gradient(180deg,#1e8ed3 0%,#2a86bf 45%,#1a77b4 100%)}
.featured-title{position:absolute;left:0;width:1200px;top:88px;text-align:center;color:var(--white);font-family:"Lato",sans-serif;font-weight:700;font-size:31px}
.featured-rule{position:absolute;left:567px;top:145px;background:var(--white)}
.card{position:absolute;top:196px;width:232px;height:313px;background:var(--white);text-align:center;padding:0 20px}
.card-icon{width:76px;height:76px;margin:24px auto 0;border-radius:50%;background:#eaf5fb;display:flex;align-items:center;justify-content:center}
.card h3{font-family:"Lato",sans-serif;font-weight:700;font-size:16px;color:var(--ink);margin-top:18px}
.card p{font-size:12px;line-height:21px;margin-top:12px;color:#777}
.card .more{display:block;margin-top:10px;font-size:12px;color:var(--blue);font-weight:500}

/* doing */
.doing-title{position:absolute;left:110px;top:1893px}
.doing-rule{position:absolute;left:110px;top:1946px}
.doing-text{position:absolute;left:110px;top:1972px;width:475px;font-size:13px;line-height:28.5px;text-align:justify}
.video{position:absolute;left:617px;top:1905px;width:470px;height:251px;background:radial-gradient(circle at 50% 55%,#6f9b5b 0%,#9fb79a 25%,#c9d4d8 55%,#aeb9bf 100%);box-shadow:0 8px 20px rgba(0,0,0,.18)}
.play{position:absolute;left:210px;top:100px;width:50px;height:50px;border-radius:50%;background:var(--white);display:flex;align-items:center;justify-content:center}

/* recent work */
.recent{position:absolute;left:0;top:2257px;width:1200px;height:876px;background:var(--light)}
.recent-title{position:absolute;left:0;width:1200px;top:88px;text-align:center}
.recent-rule{position:absolute;left:570px;top:141px}
.tile{position:absolute;height:263px}
.tile-label{position:absolute;left:40px;top:152px;color:var(--white);font-family:"Lato",sans-serif;font-size:20px;line-height:34px}
.tile-label::before{content:"";display:block;width:26px;height:2px;background:var(--white);margin-bottom:6px}
.tile-label b{display:block;font-weight:700}

/* stats */
.stats{position:absolute;left:0;top:3133px;width:1200px;height:366px;background:var(--green-stat)}
.stat{position:absolute;top:62px;width:200px;text-align:center;color:var(--white)}
.stat-ring{width:158px;height:158px;margin:0 auto;border-radius:50%;border:4px solid var(--white);display:flex;align-items:center;justify-content:center}
.stat-core{width:132px;height:132px;border-radius:50%;background:var(--white);display:flex;align-items:center;justify-content:center}
.stat-num{font-family:"Lato",sans-serif;font-size:33px;margin-top:10px}
.stat-label{font-size:12px;margin-top:2px;letter-spacing:.3px}
.ribbon{position:absolute;left:353px;top:3467px;width:492px;height:63px}
.ribbon-text{position:absolute;left:353px;top:3467px;width:492px;height:63px;display:flex;align-items:center;justify-content:center;color:var(--white);font-family:"Lato",sans-serif;font-weight:700;font-size:20px}

/* chart */
.chart-title{position:absolute;left:0;width:1200px;top:3625px;text-align:center;font-family:"Lato",sans-serif;font-weight:700;font-size:31px;color:var(--ink)}
.map-art{position:absolute;left:215px;top:3690px;width:855px;height:440px;background:radial-gradient(ellipse at 50% 50%,#eceef0 0%,#f4f5f6 60%,#ffffff 85%)}
.chart{position:absolute;left:0;top:3700px}

/* subscribe */
.subscribe{position:absolute;left:0;top:4165px;width:1200px;height:74px;background:var(--blue)}
.sub-label{position:absolute;left:323px;top:24px;color:var(--white);font-family:"Lato",sans-serif;font-weight:700;font-size:20px}
.sub-input{position:absolute;left:512px;top:19px;width:238px;height:36px;background:var(--white);font-size:11px;color:#888;padding:11px 10px}
.sub-btn{position:absolute;left:758px;top:19px;width:92px;height:36px;background:var(--orange);color:var(--white);font-size:12px;font-weight:700;display:flex;align-items:center;justify-content:center}

/* footer */
.site-footer{position:absolute;left:0;top:4239px;width:1200px;height:313px;background:linear-gradient(180deg,#3a3d3f 0%,var(--footer) 100%);color:#d8d8d8;font-size:12px}
.foot-brand{position:absolute;left:111px;top:80px;font-family:"Lato",sans-serif;font-weight:900;font-size:20px;color:var(--blue);letter-spacing:1px}
.foot-dot{position:absolute;left:145px;top:30px;width:42px;height:42px;border-radius:50%;background:var(--green)}
.copy{position:absolute;left:111px;top:142px;line-height:22px;font-size:11px}
.social{position:absolute;left:111px;top:222px;display:flex;gap:20px}
.social span{width:20px;height:20px;border-radius:50%;background:#e6e6e6}
.foot-col{position:absolute;top:40px}
.foot-col h4{font-size:12px;font-weight:700;color:var(--white);margin-bottom:14px}
.foot-col li{list-style:none;line-height:34.5px}
.contact li{display:flex;gap:18px}
.contact li i{width:12px;font-style:normal}
</style>
</head>
<body>

<header class="site-header">
  <div class="brand-dot"></div>
  <div class="brand">CORVANE<br>COLLECTIVE</div>
  <div class="call">
    <span class="call-icon"><svg width="18" height="18" viewBox="0 0 24 24"><path d="M6.6 10.8a15 15 0 0 0 6.6 6.6l2.2-2.2c.3-.3.7-.4 1-.2 1.1.4 2.3.6 3.6.6.6 0 1 .4 1 1V20c0 .6-.4 1-1 1A17 17 0 0 1 3 4c0-.6.4-1 1-1h3.5c.6 0 1 .4 1 1 0 1.3.2 2.5.6 3.6.1.3 0 .7-.2 1z" fill="var(--blue)"/></svg></span>
    <span>Call us Today : <strong>+1 555 014 2200</strong></span>
  </div>
  <nav class="nav">
    <a class="active" style="left:0">Home</a>
    <a style="left:88px">About us</a>
    <a style="left:194px">Projects</a>
    <a style="left:295px">Causes</a>
    <a style="left:390px">Events</a>
    <a style="left:482px">Contact Us</a>
  </nav>
  <a class="btn quote">Request Quote</a>
</header>

<section class="hero" role="img" aria-label="Snow-capped mountain above a forested lake with reflections">
  <div class="hero-panel"></div>
  <div class="hero-kicker">CLIMATE ADAPTATION</div>
  <h1 class="hero-title">IMPLEMENTING<br>CLIMATE STRATEGIES</h1>
  <a class="btn hero-btn">GET STARTED</a>
  <div class="dots"><span></span><span class="on"></span><span></span></div>
</section>

<section class="about">
  <div class="about-art" role="img" aria-label="Illustration of a tree with a blue trunk and green leaves"></div>
  <h2 class="section-title about-title">ABOUT <span>CORVANECOLLECTIVE</span></h2>
  <div class="rule about-rule"></div>
  <p class="about-text">Founded in 2019, the Corvane Collective draws from decades of commitment and action. A core group of committed professionals and community leaders have come together to grow and build a network of people who want to secure our next generations future. Members of the Collective come from all backgrounds and ages, but all commonly believe we can no longer be just “scribes and witnesses” to the pending demise.We believe in answering the call to action.</p>
  <a class="btn vision">OUR VISION</a>
  <a class="btn volunteers">VOLUNTEERS</a>
</section>

<section class="featured" role="img" aria-label="Blue-tinted forest backdrop">
  <h2 class="featured-title">FEATURED PROJECTS</h2>
  <div class="rule featured-rule"></div>
  <article class="card" style="left:111px">
    <div class="card-icon"><svg width="44" height="44" viewBox="0 0 44 44" fill="none" stroke="var(--blue)" stroke-width="2"><circle cx="22" cy="22" r="14"/><path d="M15 27v-5M20 27v-8M25 27v-6M30 27v-10" stroke="var(--green)"/></svg></div>
    <h3>Adaptation Plans</h3>
    <p>Communities throughout the region have adopted plans to to address our changing climate. Many more are in the process of developing plans.</p>
    <a class="more">Learn More ➜</a>
  </article>
  <article class="card" style="left:359px">
    <div class="card-icon"><svg width="44" height="44" viewBox="0 0 44 44" fill="none" stroke="var(--blue)" stroke-width="2"><circle cx="22" cy="22" r="15" stroke-dasharray="4 3"/><circle cx="22" cy="22" r="8" stroke="var(--green)"/></svg></div>
    <h3>On The Ground....</h3>
    <p>The Alliance is familiar and growing throughout the region. Presently our work has us on the ground in keystone watersheds in the Cascade</p>
    <a class="more">Learn More ➜</a>
  </article>
  <article class="card" style="left:607px">
    <div class="card-icon"><svg width="44" height="44" viewBox="0 0 44 44" fill="none" stroke="var(--blue)" stroke-width="2"><path d="M22 8a10 10 0 0 1 6 18v5h-12v-5a10 10 0 0 1 6-18z"/><path d="M22 14v10M18 19l4 4 4-4" stroke="var(--green)"/><path d="M17 35h10"/></svg></div>
    <h3>Ecological Resilience</h3>
    <p>To endure change Communities need to keep their watersheds functioning. Our network or professionals have decades</p>
    <a class="more">Learn More ➜</a>
  </article>
  <article class="card" style="left:855px">
    <div class="card-icon"><svg width="44" height="44" viewBox="0 0 44 44" fill="none" stroke="var(--blue)" stroke-width="2"><path d="M16 8l-6 14h7l-4 14 12-18h-7l5-10z"/><rect x="27" y="16" width="9" height="18" rx="2" stroke="var(--green)"/></svg></div>
    <h3>Energy And Food</h3>
    <p>Security of community food and energy have, and always will be, an essential component of how communities sustain themselves.</p>
    <a class="more">Learn More ➜</a>
  </article>
</section>

<section class="doing">
  <h2 class="section-title doing-title">WHAT WE <span>ARE DOING ?</span></h2>
  <div class="rule doing-rule"></div>
  <p class="doing-text">Lorem ipsum dolor sit amet, consectetur adipiscing elit, sed do eiusmod tempor incididunt ut labore et dolore magna aliqua. Ut enim ad minim veniam, quis nostrud exercitation ullamco laboris nisi ut aliquip ex ea commodo consequat. Duis aute irure dolor in reprehenderit in voluptate velit esse cillum dolore eu fugiat nulla pariatur. Excepteur sint occaecat cupidatat non proident, sunt in culpa qui</p>
  <div class="video" role="img" aria-label="Video still: hand holding a glass sphere reflecting a forest">
    <span class="play"><svg width="16" height="16" viewBox="0 0 16 16"><path d="M4 2l10 6-10 6z" fill="var(--blue)"/></svg></span>
  </div>
</section>

<section class="recent">
  <h2 class="section-title recent-title">RECENT <span>WORK</span></h2>
  <div class="rule recent-rule"></div>
  <div class="tile" style="left:111px;top:183px;width:465px;background:linear-gradient(180deg,#c7ccd2 0%,#e2d6c6 60%,#b59c86 100%)" role="img" aria-label="Wind turbine against a pale dusk sky">
    <div class="tile-label">ENERGY<b>Investing in clean energy</b></div>
  </div>
  <div class="tile" style="left:620px;top:183px;width:467px;background:linear-gradient(180deg,#4a4d50 0%,#6d7278 45%,#8a8f5a 100%)" role="img" aria-label="Hand placing a sky panel over a grey field">
    <div class="tile-label">FOOD SECURITY<b>Retooling agriculture/span&gt;</b></div>
  </div>
  <div class="tile" style="left:111px;top:489px;width:465px;background:linear-gradient(160deg,#9a7a4e 0%,#5f6b78 45%,#7c6a4c 100%)" role="img" aria-label="Aerial view of a river delta and autumn wetlands">
    <div class="tile-label">ECOLOGICAL RESILIENCE<b>Environmental Progress</b></div>
  </div>
  <div class="tile" style="left:620px;top:489px;width:467px;background:linear-gradient(180deg,#1f2e27 0%,#39403f 50%,#5a5f60 100%)" role="img" aria-label="Road with cars winding through a dark forest">
    <div class="tile-label">INFRASTRUCTURE<b>Lorem Ipsum</b></div>
  </div>
</section>

<section class="stats">
  <div class="stat" style="left:128px">
    <div class="stat-ring"><div class="stat-core"><svg width="54" height="54" viewBox="0 0 54 54" fill="none" stroke="#555" stroke-width="2"><rect x="14" y="8" width="26" height="32" rx="2"/><path d="M19 16h16M19 22h16M19 28h10"/></svg></div></div>
    <div class="stat-num">250 +</div><div class="stat-label">PROJECTS COMPLETED</div>
  </div>
  <div class="stat" style="left:374px">
    <div class="stat-ring"><div class="stat-core"><svg width="54" height="54" viewBox="0 0 54 54" fill="none" stroke="#555" stroke-width="2"><path d="M27 40s-12-8-12-16a6 6 0 0 1 12-2 6 6 0 0 1 12 2c0 8-12 16-12 16z"/></svg></div></div>
    <div class="stat-num">300 +</div><div class="stat-label">DONATIONS</div>
  </div>
  <div class="stat" style="left:619px">
    <div class="stat-ring"><div class="stat-core"><svg width="54" height="54" viewBox="0 0 54 54" fill="none" stroke="#555" stroke-width="2"><path d="M18 10h18v8a9 9 0 0 1-18 0z"/><path d="M27 27v8M20 42h14v-7H20z"/></svg></div></div>
    <div class="stat-num">17 +</div><div class="stat-label">COMMUNITIES ENGAGED</div>
  </div>
  <div class="stat" style="left:865px">
    <div class="stat-ring"><div class="stat-core"><svg width="54" height="54" viewBox="0 0 54 54" fill="none" stroke="#555" stroke-width="2"><circle cx="27" cy="20" r="7"/><path d="M14 44c0-8 6-13 13-13s13 5 13 13"/></svg></div></div>
    <div class="stat-num">70 +</div><div class="stat-label">VOLUNTEERS</div>
  </div>
</section>
<svg class="ribbon" viewBox="0 0 492 63" aria-hidden="true"><polygon points="0,0 492,0 462,31.5 492,63 0,63 30,31.5" fill="var(--orange)"/></svg>
<a class="ribbon-text">JOIN US TODAY</a>

<section class="savings">
  <h2 class="chart-title">THINK GREEN ! SAVE MONEY</h2>
  <div class="map-art" role="img" aria-label="Faint grey regional map backdrop"></div>
  <svg class="chart" width="1200" height="440" viewBox="0 3700 1200 440" font-family="Roboto, sans-serif">
    <g font-size="20" fill="var(--blue)" text-anchor="middle">
      <text x="419" y="3750">98%</text><text x="540" y="3826">56%</text>
      <text x="667" y="3791">77%</text><text x="797" y="3750">84%</text>
    </g>
    <polygon points="384,3804 419,3774 454,3804 419,3834" fill="#b5d96a"/>
    <polygon points="384,3804 419,3834 419,4040 384,4010" fill="#8cbf3a"/>
    <polygon points="419,3834 454,3804 454,4010 419,4040" fill="#9fcd46"/>
    <polygon points="509,3892 544,3862 579,3892 544,3922" fill="#3ab0ea"/>
    <polygon points="509,3892 544,3922 544,4040 509,4010" fill="#0a8fd4"/>
    <polygon points="544,3922 579,3892 579,4010 544,4040" fill="#0f9ee6"/>
    <polygon points="636,3848 671,3818 706,3848 671,3878" fill="#f9984a"/>
    <polygon points="636,3848 671,3878 671,4040 636,4010" fill="#ee6f1b"/>
    <polygon points="671,3878 706,3848 706,4010 671,4040" fill="#f47a20"/>
    <polygon points="760,3830 795,3800 830,3830 795,3860" fill="#5e8fe0"/>
    <polygon points="760,3830 795,3860 795,4040 760,4010" fill="#2f68c9"/>
    <polygon points="795,3860 830,3830 830,4010 795,4040" fill="#3d77d6"/>
    <g font-size="18" fill="var(--white)">
      <text x="390" y="4020">01</text><text x="515" y="4020">02</text>
      <text x="642" y="4020">03</text><text x="766" y="4020">04</text>
    </g>
    <g font-size="15" fill="var(--ink)" text-anchor="middle">
      <text x="409" y="4074">Clean Water</text><text x="540" y="4074">Forest Rescue</text>
      <text x="671" y="4074">Agriculture</text><text x="795" y="4074">Alternative</text>
      <text x="795" y="4100">Energy</text>
    </g>
  </svg>
</section>

<section class="subscribe">
  <div class="sub-label">SUBSCRIBE EMAIL</div>
  <div class="sub-input">Enter Email Address</div>
  <a class="sub-btn">SUBSCRIBE</a>
</section>

<footer class="site-footer">
  <div class="foot-dot"></div>
  <div class="foot-brand">CORVANE<br>COLLECTIVE</div>
  <p class="copy">Copyright © 2019, Company Name<br>All Right reserved</p>
  <div class="social"><span></span><span></span><span></span><span></span><span></span></div>
  <div class="foot-col" style="left:394px">
    <h4>QUICK LINKS</h4>
    <ul><li>Home</li><li>About Us</li><li>Causes</li><li>Testimonial</li><li>Events</li><li>Contact Us</li></ul>
  </div>
  <div class="foot-col" style="left:620px">
    <h4>Projects</h4>
    <ul><li>Adaptation Plans</li><li>On The Ground....</li><li>Ecological Resilience</li><li>Energy And Food</li></ul>
  </div>
  <div class="foot-col contact" style="left:864px">
    <h4>CONTACT INFO</h4>
    <ul>
      <li><i>●</i>218 Alder Ridge Rd, Port</li>
      <li><i></i>Tessen WA 98000</li>
      <li><i>✆</i>360-555-0148</li>
      <li><i>✉</i>info@corvanecollective.org</li>
    </ul>
  </div>
</footer>

</body>
</html>
```